Gourmet food made with love and care in my country kitchen

I'd like a business card designed for my small home-based food business. I have made labelling in federation blue for my food products (Labneh cheese, spicy pumpkin chutney, dukkah, caramelised onion jam, yo-Yo biscuits, chocolate mud cake etc) and have navy and white checked surrounds/borders on my brochures so would like to stick to these country colours.
Target Market(s)
Foodies who love gourmet delicacies. Everyone who enjoys a picnic that they don't have to prepare themselves.
Industry/Entity Type
Business
Contact Information for Business Card
Larkhollow Pantry
42 Tindale's Lane
Brimsworth Qld 4829
Phone Viv 07 48216597 or 0412386951
- Harrington

```html
<!DOCTYPE html>
<html lang="en">
<head>
<meta charset="utf-8">
<title>Larkhollow Pantry – Business Card</title>
<link rel="stylesheet" href="https://fonts.googleapis.com/css2?family=Princess+Sofia&family=Yellowtail&display=swap">
<style>
  :root {
    --federation-blue: #0c47f7;
    --sky-band: #8ac1f2;
    --card-white: #ffffff;
  }
  html, body {
    margin: 0;
    padding: 0;
    width: 1200px;
    height: 741px;
    overflow: hidden;
    background: var(--federation-blue);
  }
  .card {
    position: relative;
    width: 1200px;
    height: 741px;
    background: var(--federation-blue);
    overflow: hidden;
  }
  .business-name {
    position: absolute;
    left: 0;
    top: 0;
    margin: 0;
    font-family: "Princess Sofia", cursive;
    font-weight: 400;
    color: var(--card-white);
    font-size: 150px;
    line-height: 1;
  }
  .business-name .line {
    position: absolute;
    white-space: nowrap;
  }
  .business-name .line-first {
    left: 24px;
    top: 300px;
  }
  .business-name .line-second {
    left: 116px;
    top: 470px;
  }
  .service-band {
    position: absolute;
    left: 0;
    top: 642px;
    width: 1200px;
    height: 99px;
    background: var(--sky-band);
  }
  .services {
    position: absolute;
    left: 0;
    top: 660px;
    margin: 0;
    padding: 0;
    list-style: none;
    font-family: "Yellowtail", cursive;
    font-size: 34px;
    color: var(--card-white);
    line-height: 1;
  }
  .services li {
    position: absolute;
    white-space: nowrap;
  }
  .services .market-food { left: 156px; }
  .services .picnic-hampers { left: 470px; }
  .services .cooking-classes { left: 834px; }
</style>
</head>
<body>
  <main class="card">
    <div class="service-band"></div>
    <h1 class="business-name">
      <span class="line line-first">Larkhollow</span>
      <span class="line line-second">Pantry</span>
    </h1>
    <ul class="services">
      <li class="market-food">Gourmet market food</li>
      <li class="picnic-hampers">Vintage Picnic Hampers</li>
      <li class="cooking-classes">Cooking Classes</li>
    </ul>
  </main>
</body>
</html>
```